LEAP GLIDE SOAR

Need a 4 X 6 post card design. Here are the elements that need to be on the card:
LEAP, GLIDE, SOAR (This is the title please feel free and create)
DATE: August 28, 2022
Showtimes 2:30 PM & 7:30 PM
Location: Harriet Colvane Theatre Walnut Creek, CA
Tickets can be purchased at:
http://colvanestagehall.tixora-example.com/LEAPGLIDESOAR or
by calling the ticket office at (925) 555-STAGE
LEAP, GLIDE, SOAR showcases the dance stylings of urban hip hop, ballet, modern jazz and much much more! Bay Area renown dancer/choreographer Rosa Janelle Pruitt headlines this cast of dancers and will amaze you as she takes you on a journey through dance that you will never forget. Join us for an experience that will prove to excite and delight you!
Now for the artwork I would like to incorporate all three of these photos. The photo entitled "beach" you are only to use the dancer on the left. So clip out the other dancer in the pink dress. The Garden photo and the beach photo the images need to be cut out from the background. The sidewalk photo you can leave the background (just my preference) but for the sake of the overall design I'm ok with removing its background as well.
Ok have at it. I want to end this competition in a few days so let's get these designs in. Thank you!

```html
<!DOCTYPE html>
<html lang="en">
<head>
<meta charset="utf-8">
<title>LEAP GLIDE SOAR – Postcard</title>
<link rel="stylesheet" href="https://fonts.googleapis.com/css2?family=Rubik+Dirt&family=Quicksand:wght@500;600&display=swap">
<style>
  :root {
    --night-deep: #0b0f1c;
    --night-blue: #13284a;
    --street-teal: #2b7fa6;
    --letter-ivory: #ece0dc;
    --cloth-violet: #9a86c9;
    --dancer-white: #e9e4ea;
    --dancer-grey: #8d8a90;
    --dress-pink: #ff3fbf;
    --info-ivory: #f1ebe8;
  }
  html, body {
    margin: 0;
    padding: 0;
    overflow: hidden;
    background: var(--night-deep);
  }
  .postcard {
    position: relative;
    width: 800px;
    height: 1200px;
    overflow: hidden;
    background: var(--night-deep);
  }
  .artwork {
    position: absolute;
    inset: 0;
    display: block;
  }
  .title-word {
    font-family: "Rubik Dirt", "Impact", sans-serif;
    fill: var(--letter-ivory);
  }
  .event-info {
    position: absolute;
    left: 60px;
    right: 60px;
    top: 858px;
    font-family: "Quicksand", "Helvetica Neue", sans-serif;
    color: var(--info-ivory);
    text-align: center;
  }
  .event-info p { margin: 0; }
  .event-date {
    font-size: 17px;
    font-weight: 600;
    letter-spacing: 2px;
    text-transform: uppercase;
  }
  .showtimes {
    font-size: 20px;
    font-weight: 600;
    letter-spacing: 0.2px;
    margin-top: 6px !important;
  }
  .tickets {
    font-size: 13.5px;
    font-weight: 500;
    line-height: 1.35;
    margin-top: 8px !important;
  }
  .tickets span { display: block; }
  .description {
    font-size: 13px;
    font-weight: 500;
    line-height: 1.45;
    margin-top: 18px !important;
    opacity: 0.9;
  }
</style>
</head>
<body>
<main class="postcard">
  <svg class="artwork" width="800" height="1200" viewBox="0 0 800 1200" xmlns="http://www.w3.org/2000/svg">
    <defs>
      <radialGradient id="street-glow" cx="0.15" cy="0.55" r="0.7">
        <stop offset="0" stop-color="var(--street-teal)" stop-opacity="0.75"/>
        <stop offset="0.45" stop-color="var(--night-blue)" stop-opacity="0.8"/>
        <stop offset="1" stop-color="var(--night-deep)"/>
      </radialGradient>
      <linearGradient id="cloth-fade" x1="0" y1="0" x2="1" y2="0">
        <stop offset="0" stop-color="var(--cloth-violet)"/>
        <stop offset="0.7" stop-color="var(--dancer-white)"/>
      </linearGradient>
      <linearGradient id="second-dancer" x1="0" y1="0" x2="0" y2="1">
        <stop offset="0" stop-color="var(--dancer-white)"/>
        <stop offset="1" stop-color="var(--dancer-grey)"/>
      </linearGradient>
      <linearGradient id="info-shade" x1="0" y1="0" x2="0" y2="1">
        <stop offset="0" stop-color="var(--night-deep)" stop-opacity="0"/>
        <stop offset="0.3" stop-color="var(--night-deep)" stop-opacity="0.6"/>
        <stop offset="1" stop-color="var(--night-deep)" stop-opacity="0.85"/>
      </linearGradient>
      <clipPath id="title-clip">
        <text class="title-word" x="68" y="370" font-size="390" textLength="665" lengthAdjust="spacingAndGlyphs">LEAP</text>
        <text class="title-word" x="68" y="592" font-size="290" textLength="665" lengthAdjust="spacingAndGlyphs">GLIDE</text>
        <text class="title-word" x="68" y="822" font-size="320" textLength="665" lengthAdjust="spacingAndGlyphs">SOAR</text>
      </clipPath>
    </defs>

    <rect class="street-backdrop" width="800" height="1200" fill="url(#street-glow)" role="img" aria-label="Night street photograph with blurred light trails"/>
    <rect class="info-shade" x="0" y="820" width="800" height="380" fill="url(#info-shade)"/>

    <g class="title-streaks" fill="var(--letter-ivory)">
      <rect x="0" y="118" width="58" height="7" rx="3"/>
      <rect x="0" y="364" width="62" height="6" rx="3"/>
      <rect x="0" y="470" width="50" height="6" rx="3"/>
      <rect x="0" y="584" width="66" height="6" rx="3"/>
      <rect x="0" y="790" width="56" height="7" rx="3"/>
      <rect x="738" y="98" width="62" height="6" rx="3"/>
      <rect x="745" y="226" width="55" height="6" rx="3"/>
      <rect x="740" y="420" width="60" height="6" rx="3"/>
      <rect x="735" y="590" width="65" height="7" rx="3"/>
      <rect x="742" y="770" width="58" height="6" rx="3"/>
    </g>

    <g class="title">
      <text class="title-word" x="68" y="370" font-size="390" textLength="665" lengthAdjust="spacingAndGlyphs">LEAP</text>
      <text class="title-word" x="68" y="592" font-size="290" textLength="665" lengthAdjust="spacingAndGlyphs">GLIDE</text>
      <text class="title-word" x="68" y="822" font-size="320" textLength="665" lengthAdjust="spacingAndGlyphs">SOAR</text>
    </g>

    <g class="dancer-photos" clip-path="url(#title-clip)">
      <rect x="80" y="93" width="520" height="280" fill="url(#cloth-fade)" role="img" aria-label="Dancer in white raising a violet cloth overhead"/>
      <rect x="455" y="130" width="280" height="470" fill="url(#second-dancer)" role="img" aria-label="Dancer with braided hair reaching upward"/>
      <rect x="130" y="390" width="223" height="440" fill="var(--dress-pink)" role="img" aria-label="Headline dancer standing in a pink dress"/>
    </g>
  </svg>

  <section class="event-info">
    <p class="event-date">August 28, 2022</p>
    <p class="showtimes">2:30 PM &amp; 7:30 PM &nbsp;/&nbsp; Harriet Colvane Theatre Walnut Creek, CA</p>
    <p class="tickets">
      <span>Tickets can be purchased at: http://colvanestagehall.tixora-example.com/LEAPGLIDESOAR or</span>
      <span>by calling the ticket office at (925) 555-STAGE</span>
    </p>
    <p class="description">LEAP, GLIDE, SOAR showcases the dance stylings of urban hip hop, ballet, modern jazz and much much more! Bay Area renown dancer/choreographer Rosa Janelle Pruitt headlines this cast of dancers and will amaze you as she takes you on a journey through dance that you will never forget. Join us for an experience that will prove to excite and delight you!</p>
  </section>
</main>
</body>
</html>
```